Forge Night Club Flyer, need asap for party this weekend

Need a flyer for club night this Saturday. Guaranteed project need quick turnaround. Image attached, and the FORGE logo to be large and detailed like a sign. The dj names MERIDAN, MR. KALTOVE, AND DESMOND R. FALLOWAY can be large too. It's for house/electronic music in a nice classy venue. High Res image attached.

Target Market(s)

21-40 year old house music lovers, club business

Industry/Entity Type

Night Club

Font styles to use
Sans Serif

Colors
ffffff
cadf82
33a6d7
0356a4
fbee3d

Requirements
Must have
• Either the girl in hard hat or tool belt image, or something similar to stick with the Forge theme. Also the dj names needs to be the same size
Nice to have
• Faded image or some lining around the images so it doesn't look like a plain photo. Black and white is good or faded.
Should not have
• Any cursive or anything not professional looking

```html
<!DOCTYPE html>
<html lang="en">
<head>
<meta charset="utf-8">
<title>Forge — Club Night Flyer</title>
<link href="https://fonts.googleapis.com/css2?family=Anton&family=Josefin+Sans:wght@300;400;600;700&display=swap" rel="stylesheet">
<style>
  :root {
    --stage: #8f8f8f;
    --night-deep: #120a06;
    --night-warm: #3a2214;
    --gold: #f2a712;
    --band-yellow: #fbde05;
    --band-light: #fff36a;
    --ink: #1a1208;
    --white: #ffffff;
    --title: #f3efe9;
    --photo-light: #c99268;
    --photo-mid: #a8683e;
  }
  * { margin: 0; padding: 0; box-sizing: border-box; }
  html, body { width: 1200px; height: 900px; overflow: hidden; }
  body {
    background: var(--stage);
    position: relative;
    font-family: "Josefin Sans", sans-serif;
  }
  .flyer {
    position: absolute;
    left: 30px; top: 44px;
    width: 1140px; height: 812px;
    overflow: hidden;
    background:
      radial-gradient(circle at 78% 20%, rgba(200,120,60,.35), transparent 38%),
      radial-gradient(circle at 92% 68%, rgba(230,150,80,.25), transparent 30%),
      radial-gradient(circle at 60% 55%, rgba(120,60,30,.45), transparent 40%),
      linear-gradient(135deg, var(--night-warm), var(--night-deep) 70%);
  }
  .flyer__edge { position: absolute; right: 0; top: 0; width: 120px; height: 812px; }
  .hero-photo {
    position: absolute; left: 0; top: 0;
    width: 560px; height: 812px;
    background: linear-gradient(160deg, var(--photo-light), var(--photo-mid));
    -webkit-mask-image: linear-gradient(90deg, #000 82%, transparent);
            mask-image: linear-gradient(90deg, #000 82%, transparent);
  }
  .age-note {
    position: absolute; left: 915px; top: 18px;
    font-weight: 700; font-size: 14px; color: var(--white); letter-spacing: .5px;
  }
  .title {
    position: absolute; left: 570px; top: 58px;
    font-family: "Anton", sans-serif;
    font-size: 206px; line-height: 1; letter-spacing: 4px;
    color: var(--title);
  }
  .subtitle {
    position: absolute; left: 588px; top: 280px;
    font-weight: 400; font-size: 28px; color: var(--white); letter-spacing: .3px;
  }
  .lineup { position: absolute; left: 600px; top: 352px; list-style: none; }
  .lineup__act {
    font-size: 36px; line-height: 52px; color: var(--gold); font-weight: 400;
  }
  .lineup__name { color: var(--white); font-weight: 700; }
  .date { position: absolute; left: 603px; top: 568px; color: var(--white); }
  .date__month {
    position: absolute; left: 4px; top: -10px;
    font-weight: 300; font-size: 40px; letter-spacing: -1px;
    white-space: nowrap;
  }
  .date__day {
    position: absolute; left: 0; top: 26px;
    font-weight: 300; font-size: 128px; letter-spacing: -6px; line-height: 1;
    transform: scaleX(.82); transform-origin: left top;
  }
  .date__num {
    position: absolute; left: 190px; top: -25px;
    font-weight: 700; font-size: 180px; color: var(--gold); line-height: 1; letter-spacing: -6px;
  }
  .info-band {
    position: absolute; left: -10px; top: 742px;
    width: 1170px; height: 74px;
    background: linear-gradient(180deg, var(--band-light), var(--band-yellow) 55%, #f0c400);
    transform: rotate(-1.3deg);
    display: flex; align-items: flex-start; justify-content: space-between;
    padding: 16px 140px 0 90px;
    font-style: italic; font-weight: 400; font-size: 23px; color: var(--ink);
  }
</style>
</head>
<body>
  <main class="flyer">
    <svg class="flyer__edge" viewBox="0 0 120 812" aria-hidden="true">
      <polygon points="70,0 120,0 120,300 95,240" fill="#7a3410" opacity=".7"/>
      <polygon points="120,320 120,700 80,640" fill="#c0501c" opacity=".6"/>
      <polygon points="20,0 60,0 40,30" fill="#e08a2a" opacity=".8"/>
    </svg>
    <div class="hero-photo" role="img" aria-label="Photo of a woman in a cropped plaid shirt and denim wearing a leather tool belt with wrenches, pliers and a hammer"></div>

    <p class="age-note">ADULTS ONLY 21+</p>
    <h1 class="title">FORGE</h1>
    <p class="subtitle">W HOUSE + TECH WORKERS</p>

    <ul class="lineup">
      <li class="lineup__act">DJ <span class="lineup__name">MERIDAN</span></li>
      <li class="lineup__act">MR.<span class="lineup__name">KALTOVE</span></li>
      <li class="lineup__act">DESMOND R.<span class="lineup__name">FALLOWAY</span></li>
    </ul>

    <div class="date">
      <span class="date__month">MARCH</span>
      <span class="date__day">SAT</span>
      <span class="date__num">12</span>
    </div>

    <footer class="info-band">
      <span class="info-band__venue">KESTREL LOUNGE</span>
      <span class="info-band__address">712 W LARKSPUR AVE FENWICK</span>
      <span class="info-band__entry">NO COVER W/ RSVP</span>
    </footer>
  </main>
</body>
</html>
```